Marquen Premium Men's Shaving Cream Product Label . Cream packaged in a Amber Jar/Black Top Cap.

Please include information ( see Marquen design Template attachment) designed on a Round Top cap. Label Diameter: 3.125" NOTE: Design this First,
Wrap Around Label: 11.3125 x 0.875" (w x h): NOTE: Required latter after selection of Final Design Selection.
Shave Cream packaged in an 8oz Low Profile Amber Jar/Black Top Cap.
Thanks

Target Market(s)

Prime Target-Men Ages 20yrs-65yrs+ and Women 20yrs-65yrs+( they purchase ovr 55% of these Mens care products for partner/spouse/friend.

Industry/Entity Type

Personel Care/Cosmetics/NaturalHealthcare

Other font styles liked:
• At this stage if you would like to submi a desigh that would include both a Top Label and your Wrap-around label on a Amber jar/black top lid. It would be helpful to see how it would look complete. Thanks . Please refer to the updated design Graphic Template for copy and layout . Questions? Let me know. Thanks.Please now use QUILLSTONE on label designs. Thanks! Please see image attachment for added Tree Image Vector that can be added to your design instead of the Original Tree Image .

Requirements
Must have
• Look and Feel of a Quality/Premium Mens Skincare Brand with a Masculine feel but attractive to women as well ( not Macho!).Think Unisex with a Male slant.
Nice to have
• Premium/Quality/Natural Skincare & Bodycare Brand
Should not have
• Not Macho. No Cartoony or Barber Tools/Bearded Men Images. Too gimicky and over-hyped!

```html
<!DOCTYPE html>
<html lang="en">
<head>
<meta charset="utf-8">
<title>Marquen Quillstone Shaving Cream – Lid Label</title>
<link rel="stylesheet" href="https://fonts.googleapis.com/css2?family=Cinzel:wght@400;600&family=Tinos&display=swap">
<style>
  :root {
    --paper: #ffffff;
    --bark: #85665a;
    --ink: #000000;
    --cream: #ffffff;
  }
  html, body {
    margin: 0;
    padding: 0;
    width: 1109px;
    height: 1200px;
    overflow: hidden;
    background: var(--paper);
  }
  .lid-label {
    display: block;
    width: 1109px;
    height: 1200px;
  }
  .band { fill: var(--bark); }
  .rim-line { fill: none; stroke: var(--ink); stroke-width: 5; }
  .face { fill: var(--ink); }
  .divider { stroke: var(--bark); stroke-width: 2; }
  .brand-name {
    font-family: "Cinzel", serif;
    font-weight: 600;
    font-size: 52px;
    letter-spacing: 7px;
    fill: var(--cream);
  }
  .product-name {
    font-family: "Cinzel", serif;
    font-weight: 400;
    font-size: 66px;
    fill: var(--bark);
  }
  .product-type {
    font-family: "Cinzel", serif;
    font-weight: 400;
    font-size: 46px;
    fill: var(--cream);
  }
  .scent {
    font-family: "Cinzel", serif;
    font-weight: 400;
    font-size: 27px;
    fill: var(--cream);
  }
  .net-weight {
    font-family: "Tinos", serif;
    font-size: 30px;
    letter-spacing: 1px;
    fill: var(--cream);
  }
</style>
</head>
<body>
<svg class="lid-label" viewBox="0 0 1109 1200" xmlns="http://www.w3.org/2000/svg">
  <defs>
    <radialGradient id="emblem-tone" cx="50%" cy="50%" r="50%">
      <stop offset="0%" stop-color="#6b4e42"/>
      <stop offset="100%" stop-color="#2a1d18"/>
    </radialGradient>
  </defs>

  <circle class="band" cx="551" cy="599" r="513" role="img" aria-label="Brown outer band with a soft tonal leaf pattern"/>
  <circle class="rim-line" cx="551" cy="599" r="456"/>
  <circle class="face" cx="551" cy="599" r="423"/>

  <text class="brand-name" x="551" y="372" text-anchor="middle">MARQUEN</text>

  <text class="product-name" x="551" y="465" text-anchor="middle">Quillstone</text>

  <line class="divider" x1="143" y1="598" x2="462" y2="598"/>
  <line class="divider" x1="640" y1="598" x2="960" y2="598"/>
  <circle cx="551" cy="598" r="81" fill="url(#emblem-tone)" stroke="var(--bark)" stroke-width="2" stroke-dasharray="2 3" role="img" aria-label="Round emblem of a brown tree of life with spreading roots"/>

  <text class="product-type" x="551" y="750" text-anchor="middle">Shaving Cream</text>
  <text class="product-type" x="551" y="804" text-anchor="middle">Crème De Rasage</text>

  <text class="scent" x="551" y="870" text-anchor="middle">Fernvale Absolut</text>
  <text class="scent" x="551" y="903" text-anchor="middle">– 1948 –</text>

  <text class="net-weight" x="551" y="987" text-anchor="middle">150g e 5.3 oz</text>
</svg>
</body>
</html>
```